Business Cards

We were billed for this because the project timed out. Please give me another designed to open this back up. I was not happy with the last designs (that I was charged for).
we are also using the logo with Revitalizing Pools One Drop at a Time
Also want to utilize Where Healthy Water is our Commitment.

Contact Information for Business Card

Marlowe Stone Group Inc

```html
<!DOCTYPE html>
<html lang="en">
<head>
<meta charset="utf-8">
<title>Marlowe Stone Group – Business Card</title>
<link rel="stylesheet" href="https://fonts.googleapis.com/css2?family=Montserrat:wght@400;500;700;800&display=swap">
<style>
  :root {
    --bg: #cdcdcd;
    --blue: #1565b3;
    --blue-light: #4fa3dc;
    --white: #ffffff;
    --ink: #1f1f1f;
    --ink-soft: #4a4a4a;
  }
  * { box-sizing: border-box; margin: 0; padding: 0; }
  html, body {
    width: 1200px; height: 802px; overflow: hidden;
    background: var(--bg);
    font-family: "Montserrat", sans-serif;
  }
  .sheet {
    width: 1200px; height: 802px;
    display: flex; align-items: center; justify-content: center; gap: 40px;
  }
  .card {
    position: relative;
    width: 540px; height: 315px;
    border-radius: 22px;
    overflow: hidden;
    box-shadow: 0 12px 28px rgba(0,0,0,0.25);
  }
  /* front */
  .card-front { background: var(--white); }
  .card-front .wave { position: absolute; inset: 0; width: 100%; height: 100%; }
  .brand {
    position: absolute; top: 42px; left: 90px; width: 330px;
    text-align: center;
  }
  .brand-name {
    display: flex; align-items: center; justify-content: center; gap: 8px;
    font-weight: 800; font-size: 20px; letter-spacing: 1px; white-space: nowrap;
    color: var(--ink); text-transform: uppercase;
  }
  .brand-mark {
    width: 11px; height: 11px; background: var(--blue); border-radius: 50%; flex: none;
  }
  .brand-tagline {
    margin-top: 5px; white-space: nowrap;
    font-size: 8.5px; font-weight: 500; letter-spacing: 1.6px;
    color: var(--ink-soft); text-transform: uppercase;
  }
  .person {
    position: absolute; left: 34px; top: 192px;
  }
  .person-name {
    font-weight: 700; font-size: 19px; line-height: 24px; letter-spacing: 1.5px;
    color: var(--blue-light); text-transform: uppercase; white-space: nowrap;
  }
  .person-title {
    font-size: 12px; line-height: 16px; color: var(--white);
  }
  .rule { width: 14px; height: 1px; background: var(--blue-light); margin: 6px 0 5px; }
  .contact-list { list-style: none; }
  .contact-list li {
    display: flex; align-items: center; gap: 8px; white-space: nowrap;
    color: var(--white); font-size: 12px; line-height: 18px;
  }
  .contact-list svg { width: 11px; height: 11px; flex: none; }
  .address {
    position: absolute; right: 30px; top: 152px;
    color: var(--white); font-size: 12px; line-height: 18px; text-align: right;
  }
  /* back */
  .card-back { background: var(--blue); }
  .pattern {
    position: absolute; inset: 0;
    background: linear-gradient(135deg, #1a63ad 0%, #2b74c0 45%, #4b8fd3 100%);
  }
  .back-content {
    position: absolute; inset: 0;
    display: flex; flex-direction: column; align-items: center; justify-content: center;
  }
  .back-name {
    display: flex; align-items: center; gap: 8px;
    color: var(--white); font-weight: 800; font-size: 22px; letter-spacing: 1px;
    text-transform: uppercase;
  }
  .back-name .brand-mark { background: var(--white); }
  .back-tagline {
    margin-top: 44px;
    color: var(--white); font-size: 15px; font-weight: 500; letter-spacing: 3px;
  }
</style>
</head>
<body>
<main class="sheet">
  <section class="card card-front">
    <svg class="wave" viewBox="0 0 540 315" preserveAspectRatio="none" aria-hidden="true">
      <path d="M0 166 C120 156 220 166 330 141 C440 116 510 71 540 8 L540 315 L0 315 Z" fill="#4fa3dc"/>
      <path d="M0 173 C120 163 220 173 330 148 C440 123 510 78 540 15 L540 315 L0 315 Z" fill="#ffffff"/>
      <path d="M0 178 C120 168 220 178 330 153 C440 128 510 83 540 20 L540 315 L0 315 Z" fill="#1565b3"/>
    </svg>
    <div class="brand">
      <div class="brand-name"><span class="brand-mark"></span>Marlowe Stone Group</div>
      <div class="brand-tagline">Revitalizing Pools One Drop at a Time</div>
    </div>
    <div class="address">48 Harbor Lane, Suite 210<br>Ridgeview, AB 40218</div>
    <div class="person">
      <div class="person-name">Daniel Reyes</div>
      <div class="person-title">CEO/Founder</div>
      <div class="rule"></div>
      <ul class="contact-list">
        <li><svg viewBox="0 0 12 12"><path d="M2.5 1l2 2.2-1 1.3a6 6 0 0 0 4 4l1.3-1L11 9.5 9.6 11C5 11 1 7 1 2.4z" fill="#4fa3dc"/></svg>555-204-7731</li>
        <li><svg viewBox="0 0 12 12"><rect x="1" y="2.5" width="10" height="7" rx="1" fill="#4fa3dc"/><path d="M1.5 3l4.5 3.5L10.5 3" stroke="#1565b3" fill="none"/></svg>info@marlowestonegroup.com</li>
        <li><svg viewBox="0 0 12 12"><circle cx="6" cy="6" r="5" fill="#4fa3dc"/><path d="M1 6h10M6 1c2 2.5 2 7.5 0 10M6 1c-2 2.5-2 7.5 0 10" stroke="#1565b3" stroke-width=".8" fill="none"/></svg>www.marlowestonegroup.com</li>
      </ul>
    </div>
  </section>

  <section class="card card-back">
    <div class="pattern" role="img" aria-label="Repeating embossed brand-mark pattern in tones of blue"></div>
    <div class="back-content">
      <div class="back-name"><span class="brand-mark"></span>Marlowe Stone Group</div>
      <div class="back-tagline">Healthy Water is our Commitment</div>
    </div>
  </section>
</main>
</body>
</html>
```